Business Card Design Project

Mabel's Tonics is a natural skincare business and we need a business card designed. The company focuses on natural products and will be launching with body scrubs and bath fizzies and our mission statement is: To deliver high quality natural beauty products at a good value. It's two cards - one design - the only information changing would be name and email address

Target Market(s)

Females ages 20-50

Industry/Entity Type

Business

Requirements
Must have
• Mabel's Tonics

Corinne Halvorsen-Pitt
T: 800-417-9368
E: Corinne@MabelsTonics.example
W: www.MabelsTonics.example

Ulrich Benedetti
T: 800-417-9368
E: Ulrich@MabelsTonics.example
W: www.MabelsTonics.example
Nice to have
• I'd like to use the colors or text found at www.mabelstonics.example but I'm open to suggestions since design isn't set in stone yet. I would also like to have the words .....a little bit of magic somewhere under the company name in a different type of font. I would like a design that feels clean and maybe a retro feel to it - front and back would be nice but not mandatory

```html
<!DOCTYPE html>
<html lang="en">
<head>
<meta charset="utf-8">
<title>Mabel's Tonics — Business Card</title>
<link rel="stylesheet" href="https://fonts.googleapis.com/css2?family=Arimo:wght@400&display=swap">
<style>
  :root {
    --backdrop: #a7a9ac;
    --card: #ffffff;
    --plum: #8c1a82;
    --ink: #1a1a1a;
    --slate: #6b6b6b;
  }
  html, body {
    margin: 0;
    padding: 0;
    width: 891px;
    height: 1200px;
    overflow: hidden;
    background: var(--backdrop);
  }
  .card {
    position: absolute;
    left: 138px;
    top: 131px;
    width: 618px;
    height: 933px;
    background: var(--card);
    border-radius: 58px;
  }
  .brand {
    position: absolute;
    left: 64px;
    top: 130px;
    margin: 0;
    font-family: "Arimo", sans-serif;
    font-weight: 400;
    font-size: 58px;
    line-height: 1;
    color: var(--plum);
    white-space: nowrap;
  }
  .tagline {
    position: absolute;
    left: 66px;
    top: 226px;
    margin: 0;
    font-family: "Arimo", sans-serif;
    font-weight: 400;
    font-size: 30px;
    line-height: 1;
    color: var(--slate);
    white-space: nowrap;
  }
  .holder {
    position: absolute;
    left: 57px;
    top: 620px;
    margin: 0;
    font-family: "Arimo", sans-serif;
    font-weight: 400;
    font-size: 39px;
    line-height: 48px;
    color: var(--plum);
  }
  .holder span { display: block; }
  .rule {
    position: absolute;
    left: 57px;
    top: 742px;
    width: 500px;
    border: 0;
    border-top: 2px dotted var(--plum);
    margin: 0;
  }
  .contact {
    position: absolute;
    left: 57px;
    top: 766px;
    margin: 0;
    padding: 0;
    list-style: none;
    font-family: "Arimo", sans-serif;
    font-size: 29px;
    line-height: 36px;
    color: var(--ink);
    white-space: nowrap;
  }
</style>
</head>
<body>
  <main class="card">
    <h1 class="brand">Mabel's Tonics</h1>
    <p class="tagline">A little bit of magic</p>
    <p class="holder"><span>Corinne</span><span>Halvorsen-Pitt</span></p>
    <hr class="rule">
    <ul class="contact">
      <li>T: 800-417-9368</li>
      <li>E: Corinne@MabelsTonics.example</li>
      <li>W: www.MabelsTonics.example</li>
    </ul>
  </main>
</body>
</html>
```